New Business Card Design Project

Need a design that will create an impact / strong impression towards our clients for our business. We are in the lighting business and we do lighting retrofits for large commercial to industrial clientele.

Target Market(s)

Lighting Industry

Industry/Entity Type

Business

Font styles to use
Other font styles liked:
• we would like to use the font on our logo, not sure what it is though..

Requirements
Must have
• Our logo.
Nice to have
• We are open to suggestions that have to do with lighting.

```html
<!DOCTYPE html>
<html lang="en">
<head>
<meta charset="utf-8">
<title>Northline Retrofit Co. – Business Card</title>
<link rel="stylesheet" href="https://fonts.googleapis.com/css2?family=Open+Sans:wght@400;600&display=swap">
<style>
  :root {
    --backdrop: #3b322e;
    --card: #1b1b1c;
    --card-edge: #121213;
    --green: #2f9a45;
    --green-dark: #1f6f31;
    --text: #f2f2f2;
    --muted: #9a9a9a;
  }
  * { margin: 0; padding: 0; box-sizing: border-box; }
  html, body { width: 1200px; height: 864px; overflow: hidden; }
  body {
    background: var(--backdrop);
    font-family: "Open Sans", Arial, sans-serif;
    position: relative;
  }
  .card {
    position: absolute;
    width: 540px;
    height: 308px;
    background: var(--card);
    border: 1px solid var(--card-edge);
    box-shadow: 0 18px 40px rgba(0,0,0,.45);
  }
  .card-back { left: 50px; top: 130px; }
  .card-front { left: 610px; top: 420px; }

  /* back */
  .brand-back {
    position: absolute;
    left: 0; right: 0; top: 112px;
    display: flex; align-items: center; justify-content: center; gap: 12px;
    color: var(--green);
    font-size: 24px; font-weight: 600;
  }
  .brand-square { width: 18px; height: 18px; background: var(--green); }
  .website {
    position: absolute;
    left: 0; right: 0; top: 190px;
    text-align: center;
    color: var(--muted);
    font-size: 14px;
    letter-spacing: 2px;
  }

  /* front */
  .brand-front {
    position: absolute;
    right: 40px; top: 58px;
    display: flex; align-items: center; gap: 10px;
    color: var(--green);
    font-size: 22px; font-weight: 600;
  }
  .brand-rule {
    position: absolute;
    right: 40px; top: 100px;
    width: 300px; height: 2px;
    background: var(--green-dark);
  }
  .person {
    position: absolute;
    right: 290px; top: 168px;
    text-align: right;
    font-size: 14px; line-height: 19px;
    color: var(--text);
  }
  .person-name, .person-role { color: var(--green); text-transform: uppercase; }
  .divider {
    position: absolute;
    left: 266px; top: 170px;
    width: 1px; height: 100px;
    background: var(--muted);
  }
  .contacts {
    position: absolute;
    left: 284px; top: 172px;
    list-style: none;
    font-size: 14px; line-height: 22px;
    color: var(--text);
  }
  .contacts li { display: flex; align-items: center; gap: 10px; }
  .contacts svg { width: 12px; height: 12px; fill: var(--muted); flex: none; }
</style>
</head>
<body>
  <section class="card card-back" aria-label="Card back">
    <div class="brand-back"><span class="brand-square"></span>Northline Retrofit Co., LLC</div>
    <p class="website">www.northlineretrofit.com</p>
  </section>

  <section class="card card-front" aria-label="Card front">
    <div class="brand-front"><span class="brand-square"></span>Northline Retrofit Co., LLC</div>
    <div class="brand-rule"></div>

    <div class="person">
      <p class="person-name">Dana Whitlow</p>
      <p class="person-role">CEO/Founder</p>
      <p>4120 Birchwood Court</p>
      <p>Fairbanks, Alaska 99701</p>
    </div>

    <div class="divider"></div>

    <ul class="contacts">
      <li><svg viewBox="0 0 12 12" aria-hidden="true"><path d="M1 4c0-2 2-3 5-3s5 1 5 3l-2 1-1-1H4L3 5z M3 6h6l1 5H2z"/></svg>907 555 0142</li>
      <li><svg viewBox="0 0 12 12" aria-hidden="true"><rect x="3" y="0" width="6" height="12" rx="1"/></svg>907 555 0187</li>
      <li><svg viewBox="0 0 12 12" aria-hidden="true"><path d="M3 0h6v4H3z M0 4h12v6H0z"/></svg>907 555 0163</li>
      <li><svg viewBox="0 0 12 12" aria-hidden="true"><path d="M0 2h12v8H0z"/></svg>dana@northlineretrofit.com</li>
    </ul>
  </section>
</body>
</html>
```